Would like a Northwest feel to the look, something NOT typical of what you would see on a typical Home Inspectors logo. Real estate cards all the same as well, and would like to stand out. Earthy, green, Northwest. Sadly a portrait seems to be a requirement (see the attached). I inspect residential homes for buyers and sellers.

Target Market(s)

Home Buyers and Sellers

Industry/Entity Type

Home Inspection

Contact Information for Business Card

See description
Note: The name Corvaneth is a Chinook word that means 'Friend'. Please do not associate the name with the Whale that shows up on 99% of google searches.

Logo Text

Corvaneth Home Inspections

Colors

Designer to choose colors to be used in the design.

Requirements
Must have
• Phone Num: 541-672-8153
• Address: 732 SW 219th Av Num 618
• Portland, Oregon 97388
• Email: glen@corvanethhomeinspection.example
• Website: www.CorvanethHomeInspection.example
• Additional Note: Need to add the Obravex logo (icon). It should be small and not the focus of the card. The logo can be found at Obravex.example
Nice to have
• I am open
Should not have
• Cant think of anything

```html
<!DOCTYPE html>
<html lang="en">
<head>
<meta charset="utf-8">
<title>Corvaneth Home Inspections – Business Card</title>
<link rel="stylesheet" href="https://fonts.googleapis.com/css2?family=Open+Sans:wght@400;600;700&display=swap">
<style>
  :root {
    --backdrop: #ecebe8;
    --olive: #5b5747;
    --olive-deep: #4d493b;
    --paper: #ffffff;
    --ink: #1f1f1f;
    --cream: #f2efe6;
    --muted: #d8d4c6;
    --leaf: #34a86a;
    --seal: #9a988f;
    --shadow: 0 10px 28px rgba(0,0,0,.18);
  }
  * { box-sizing: border-box; margin: 0; padding: 0; }
  html, body { width: 1200px; height: 800px; overflow: hidden; }
  body {
    background: var(--backdrop);
    font-family: "Open Sans", Arial, sans-serif;
    position: relative;
  }
  .card {
    position: absolute;
    width: 560px;
    height: 320px;
    border-radius: 3px;
    box-shadow: var(--shadow);
    overflow: hidden;
    background: var(--olive);
  }
  /* ---------- logo side ---------- */
  .card--brand { left: 600px; top: 70px; }
  .brand-lockup {
    position: absolute;
    inset: 0;
    display: flex;
    flex-direction: column;
    align-items: center;
    justify-content: center;
    gap: 14px;
    color: var(--cream);
  }
  .brand-mark {
    width: 22px; height: 22px;
    border-radius: 50%;
    background: var(--cream);
  }
  .brand-name {
    font-weight: 700;
    font-size: 30px;
    letter-spacing: 3px;
    text-transform: uppercase;
    text-align: center;
    line-height: 1.3;
  }
  /* ---------- contact side ---------- */
  .card--contact { left: 40px; top: 410px; }
  .contact-panel {
    position: absolute;
    left: 0; top: 0;
    width: 560px; height: 320px;
  }
  .portrait {
    position: absolute;
    left: 50px; top: 48px;
    width: 128px; height: 100px;
    border: 3px solid var(--paper);
    background: linear-gradient(135deg, #6f6a44 0%, #8b8a5c 45%, #6b7458 100%);
  }
  .identity {
    position: absolute;
    left: 30px; top: 160px;
    width: 168px;
    text-align: center;
    color: var(--cream);
    line-height: 1.25;
  }
  .identity__name { font-weight: 700; font-size: 15px; }
  .identity__role, .identity__licence { font-size: 14px; color: var(--muted); }
  .contact-list {
    position: absolute;
    left: 262px; top: 82px;
    list-style: none;
    color: var(--ink);
    font-size: 13.5px;
    line-height: 1.3;
  }
  .contact-list li {
    display: flex;
    align-items: flex-start;
    gap: 12px;
    margin-bottom: 18px;
  }
  .contact-list svg { flex: none; width: 18px; height: 18px; fill: var(--leaf); margin-top: 1px; }
  .affiliate-seal {
    position: absolute;
    left: 495px; top: 40px;
    width: 38px; height: 38px;
    border-radius: 50%;
    background: var(--seal);
  }
</style>
</head>
<body>

<section class="card card--brand" aria-label="Business card front">
  <div class="brand-lockup">
    <span class="brand-mark"></span>
    <p class="brand-name">Corvaneth<br>Home Inspections</p>
  </div>
</section>

<section class="card card--contact" aria-label="Business card back">
  <svg class="contact-panel" viewBox="0 0 560 320" aria-hidden="true">
    <path d="M560 0 H330 C230 40 215 250 300 320 H560 Z" fill="#ffffff"/>
  </svg>

  <div class="portrait" role="img" aria-label="Portrait photo of Glen Corvaneth"></div>

  <div class="identity">
    <p class="identity__name">Glen Corvaneth</p>
    <p class="identity__role">Home Inspector</p>
    <p class="identity__licence">#000-000</p>
  </div>

  <span class="affiliate-seal" role="img" aria-label="Obravex member badge"></span>

  <ul class="contact-list">
    <li>
      <svg viewBox="0 0 24 24"><path d="M12 3 2 12h3v9h5v-6h4v6h5v-9h3z"/></svg>
      <span>732 SW 219th Av Num 618<br>Portland, Oregon 97388</span>
    </li>
    <li>
      <svg viewBox="0 0 24 24"><path d="M6.6 10.8a15 15 0 0 0 6.6 6.6l2.2-2.2c.3-.3.7-.4 1-.2 1.1.4 2.3.6 3.6.6.6 0 1 .4 1 1V20c0 .6-.4 1-1 1A17 17 0 0 1 3 4c0-.6.4-1 1-1h3.5c.6 0 1 .4 1 1 0 1.3.2 2.5.6 3.6.1.3 0 .7-.2 1z"/></svg>
      <span>1 (541) 672-8153</span>
    </li>
    <li>
      <svg viewBox="0 0 24 24"><path d="M2 5h20v14H2z M3 6l9 7 9-7" /><path d="M2 5l10 8 10-8" fill="#fff" opacity=".55"/></svg>
      <span>glen@corvanethhomeinspection.example</span>
    </li>
    <li>
      <svg viewBox="0 0 24 24"><circle cx="12" cy="12" r="10"/><path d="M7 6c2 1 3 3 2 5s-3 2-3 4M15 4c-1 2 0 3 2 4s3 3 2 6M12 20c0-2 1-3 3-3" stroke="#fff" stroke-width="1.4" fill="none"/></svg>
      <span>www.CorvanethHomeInspection.example</span>
    </li>
  </ul>
</section>

</body>
</html>
```